Business Card Design for general contractor or developer

General Contractors. We build new buildings as well as redesign and/or remodel existing buildings. Mostly residential, but we want to expand to commercial as well, so we want the design not to be residential specific.We want the design to be modern, but necessarily minimalistic. A monogram type is also a consideration, but would like to see all ideas.

Target Market(s)

Real estate investors, homeowners, future homeowners, commercial building owners

Industry/Entity Type

Contractor

Contact Information for Business Card

BRIMCOVE Developers Corp, 2917 NE 88th Avenue Suite 412 Coral Springs, FL 33071, Darren Kopec, (305) 555-0148, darren@brimcovedev.example

Font styles to use
Other font styles liked:
• Modern type font

Requirements
Must have
• Must be modern looking
Nice to have
• Metallic type or a standout feature
Should not have
• Tools, floorplans

```html
<!DOCTYPE html>
<html lang="en">
<head>
<meta charset="utf-8">
<title>BRIMCOVE Developers Corp – Business Card</title>
<link rel="stylesheet" href="https://fonts.googleapis.com/css2?family=Lato:wght@400;700&display=swap">
<style>
  :root {
    --page-bg: #d9d4cc;
    --card-face: #eceeec;
    --card-face-edge: #dfe3e1;
    --ink-dark: #1d2b25;
    --band-dark: #1f2e28;
    --band-mid: #2d3f37;
    --band-highlight: #8b8f8d;
    --band-text: #d6cfc2;
    --icon-tone: #b9b6ae;
  }
  * { margin: 0; padding: 0; box-sizing: border-box; }
  html, body {
    width: 1200px;
    height: 970px;
    overflow: hidden;
    background: var(--page-bg);
  }
  .business-card {
    position: absolute;
    left: 172px;
    top: 270px;
    width: 856px;
    height: 476px;
    border-radius: 22px;
    overflow: hidden;
    background: linear-gradient(180deg, var(--card-face) 0%, var(--card-face-edge) 100%);
    box-shadow: 0 6px 24px rgba(0,0,0,0.18);
    font-family: "Lato", sans-serif;
  }
  .card-band {
    position: absolute;
    left: 0;
    top: 0;
    width: 856px;
    height: 476px;
  }
  .brand-block {
    position: absolute;
    left: 40px;
    top: 150px;
    display: flex;
    align-items: center;
    gap: 12px;
  }
  .brand-mark {
    width: 22px;
    height: 22px;
    background: var(--ink-dark);
  }
  .brand-name {
    font-size: 19px;
    font-weight: 700;
    color: var(--ink-dark);
    letter-spacing: 0.1px;
  }
  .holder {
    position: absolute;
    right: 55px;
    top: 100px;
    text-align: right;
    color: var(--ink-dark);
  }
  .holder-name {
    font-size: 33px;
    font-weight: 700;
    line-height: 1.2;
  }
  .holder-role {
    font-size: 26px;
    font-weight: 400;
    line-height: 1.3;
  }
  .contact-list {
    position: absolute;
    left: 38px;
    top: 338px;
    list-style: none;
    color: var(--band-text);
    font-size: 22px;
    line-height: 31px;
  }
  .contact-list li {
    display: flex;
    align-items: center;
    gap: 7px;
  }
  .contact-icon {
    width: 20px;
    height: 20px;
    flex: none;
  }
  .office-address {
    position: absolute;
    right: 42px;
    top: 338px;
    text-align: right;
    font-style: normal;
    color: var(--band-text);
    font-size: 22px;
    line-height: 29px;
  }
</style>
</head>
<body>
  <main class="business-card">
    <svg class="card-band" viewBox="0 0 856 476" aria-hidden="true">
      <defs>
        <linearGradient id="bandFill" x1="0" y1="0" x2="0" y2="1">
          <stop offset="0" stop-color="var(--band-mid)"/>
          <stop offset="1" stop-color="var(--band-dark)"/>
        </linearGradient>
      </defs>
      <path d="M0 318 Q428 210 856 312 L856 476 L0 476 Z" fill="var(--band-highlight)"/>
      <path d="M0 328 Q428 226 856 322 L856 476 L0 476 Z" fill="url(#bandFill)"/>
    </svg>

    <div class="brand-block">
      <span class="brand-mark"></span>
      <span class="brand-name">BRIMCOVE Developers Corp</span>
    </div>

    <div class="holder">
      <p class="holder-name">Darren Kopec</p>
      <p class="holder-role">Owner</p>
    </div>

    <ul class="contact-list">
      <li>
        <svg class="contact-icon" viewBox="0 0 20 20" aria-hidden="true">
          <path d="M3 8 Q10 2 17 8 L15 10 L12.5 8.5 L12.5 7 Q10 6 7.5 7 L7.5 8.5 L5 10 Z M5 11 L15 11 L16 16 L4 16 Z" fill="var(--icon-tone)"/>
        </svg>
        <span>(305) 555-0148,</span>
      </li>
      <li>
        <svg class="contact-icon" viewBox="0 0 20 20" aria-hidden="true">
          <rect x="2" y="5" width="16" height="11" fill="var(--icon-tone)"/>
          <path d="M2.5 5.5 L10 11 L17.5 5.5" fill="none" stroke="var(--band-dark)" stroke-width="1.3"/>
        </svg>
        <span>darren@brimcovedev.example</span>
      </li>
      <li>
        <svg class="contact-icon" viewBox="0 0 20 20" aria-hidden="true">
          <g fill="none" stroke="var(--icon-tone)" stroke-width="1.4">
            <circle cx="10" cy="10" r="7.5"/>
            <ellipse cx="10" cy="10" rx="3.2" ry="7.5"/>
            <line x1="2.5" y1="10" x2="17.5" y2="10"/>
            <line x1="4" y1="6" x2="16" y2="6"/>
            <line x1="4" y1="14" x2="16" y2="14"/>
          </g>
        </svg>
        <span>www.brimcovedev.example</span>
      </li>
    </ul>

    <address class="office-address">
      2917 NE 88th Avenue<br>
      Suite 412<br>
      Coral Springs, FL 33071
    </address>
  </main>
</body>
</html>
```